Web Page Design for a Website that Provides Tutoring

I am looking to create an online tutoring website. The website will allow parents or students to contact tutors with a view to instructing them to tutor themselves or their children.

The name of the website is LendYourLessons.

This brief is to create the design for one of the web pages for this web site. I am hoping the same designer will be available to design other pages.

The page I want designed is one of the more complex and I have attached the design as an excel spreadsheet. The web page needs to include all the items on this page but if you want to change the positioning of the items then Im fine with that.

I recently had two logos created for this website. My favourite is the one with a mortar board but im not sure I like the colours. I have attached both of these logos and you can use either of them, change the colours or create something different. I just want a design pleasing to the eye. If the logo is changed I would like that in a seperate file.

So can you please submit designs for this page. I have attached the two logos which you can use, change or if you feel you have a better idea then you can use that.

On the spreadsheet the Send Message, Favourite etc are buttons.

Target Market(s)

People who want to better themselves.
Possible middle class to upper class.

Industry/Entity Type

Tutoring

Number of Pages Required

1 page

Requirements
Must have
• The designs must have alot of the information attached in the spreadsheet.

```html
<!DOCTYPE html>
<html lang="en">
<head>
<meta charset="utf-8">
<title>LendYourLessons – Tutor Profile</title>
<link href="https://fonts.googleapis.com/css2?family=Bree+Serif&family=Ubuntu:wght@400;500;700&display=swap" rel="stylesheet">
<style>
:root{
  --orange:#f07a0a;
  --orange-dark:#e06a00;
  --yellow:#f0b400;
  --green:#2e9e7a;
  --green-soft:#e4f2eb;
  --purple:#575b90;
  --purple-soft:#e9e9f5;
  --cream:#f7f1e1;
  --ink:#333;
  --muted:#666;
  --line:#e2e2e2;
  --grey-head:#555;
  --grey-row:#ededed;
  --red:#e0201a;
  --avail:#d8f7d2;
  --taken:#f4683c;
  --reserved:#f3921e;
  --no:#355a95;
  --footer:#f2f2f2;
}
*{box-sizing:border-box;margin:0;padding:0}
html,body{width:1200px;height:3130px;overflow:hidden}
body{position:relative;background:#fff;font-family:"Ubuntu",sans-serif;color:var(--ink);font-size:14px}
.abs{position:absolute}

/* header */
.site-header{left:0;top:0;width:1200px;height:84px;border-bottom:1px solid var(--line);background:#fff}
.brand{left:73px;top:24px;display:flex;align-items:center;gap:8px;font-size:30px;font-weight:700;color:var(--orange);letter-spacing:-.5px}
.brand-mark{width:14px;height:14px;background:var(--orange)}
.main-nav{left:411px;top:33px;display:flex;gap:0;font-size:14px;font-weight:500;text-transform:uppercase;color:#333}
.main-nav a{color:inherit;text-decoration:none;position:absolute;white-space:nowrap}
.main-nav a.active{color:var(--ink)}
.main-nav a.active::after{content:"";position:absolute;left:0;right:0;top:22px;height:3px;background:var(--orange)}
.login{left:956px;top:32px;font-size:14px;font-weight:500;text-transform:uppercase;display:flex;align-items:center;gap:8px}

/* hero */
.hero{left:0;top:84px;width:1200px;height:542px;background:linear-gradient(180deg,#d7dfdb 0%,#e9edeb 55%,#edefee 100%);overflow:hidden}
.hero-frame{left:75px;top:104px;width:1048px;height:460px;border:5px solid var(--green);border-bottom:none}
.hero-stripes{left:140px;top:0}
.hero-photo{left:167px;top:41px;width:333px;height:501px;border-radius:150px 150px 0 0;background:linear-gradient(180deg,#c9a07e 0%,#b88b6b 28%,#6f8fb4 45%,#5a7ca3 100%)}
.hi-bubble{left:476px;top:142px;width:96px;height:96px;border-radius:50%;background:var(--orange);color:#fff;font-family:"Bree Serif",serif;font-size:46px;display:flex;align-items:center;justify-content:center}
.hi-bubble::after{content:"";position:absolute;left:18px;bottom:-16px;border-left:14px solid transparent;border-right:14px solid transparent;border-top:24px solid var(--orange);transform:rotate(25deg)}
.hero-name{left:592px;top:170px;font-family:"Bree Serif",serif;font-size:54px;color:var(--green);letter-spacing:.5px}
.hero-role{left:594px;top:236px;font-family:"Bree Serif",serif;font-size:38px;color:#222}
.hero-text{left:595px;top:312px;width:440px;font-size:16px;line-height:26px;color:#555}
.btn{display:inline-flex;align-items:center;justify-content:center;gap:9px;color:#fff;font-size:14px;font-weight:500;text-transform:uppercase;border-radius:3px}
.hero-btn{top:446px;height:42px}
.btn-register{left:595px;width:188px;background:var(--orange)}
.btn-video{left:795px;width:194px;background:var(--green)}

/* cards */
.card{top:655px;height:322px}
.card-head{height:54px;padding:0 18px;display:flex;align-items:center;color:#fff;font-size:21px;font-weight:500}
.card-body{height:268px;padding:24px 27px 0}
.card-contact{left:73px;width:334px}
.card-contact .card-head{background:var(--yellow)}
.card-contact .card-body{background:var(--cream)}
.field{background:#fff;border:1px solid #eee;color:#aaa;font-size:13px;padding:10px 12px}
.field-subject{height:42px}
.field-message{height:108px;margin-top:10px}
.card-btn{position:absolute;left:27px;right:27px;top:253px;height:43px}
.card-contact .card-btn{background:var(--yellow)}
.card-favour{left:434px;width:332px}
.card-favour .card-head{background:var(--green)}
.card-favour .card-body{background:var(--green-soft)}
.favour-lead{font-size:14px;font-weight:700;line-height:21px;color:#333;width:240px}
.ticks{list-style:none;margin-top:14px}
.ticks li{display:flex;align-items:center;gap:10px;font-size:13px;color:#444;height:27.5px}
.card-favour .card-btn{background:var(--green)}
.card-reviews{left:793px;width:334px}
.card-reviews .card-head{background:var(--purple)}
.card-reviews .card-body{background:var(--purple-soft);padding-top:20px}
.stars{color:var(--yellow);letter-spacing:1px}
.stars .off{color:#ccc}
.rating-line{display:flex;align-items:center;gap:10px;font-size:12px;color:#444}
.bars{margin-top:14px}
.bar-row{display:flex;align-items:center;font-size:11px;color:#444;height:17px}
.bar-row span:first-child{width:48px}
.bar{width:110px;height:9px;background:#fff;margin-right:10px}
.bar i{display:block;height:100%;background:var(--yellow)}
.share-note{font-size:12px;color:#444;margin-top:12px}
.card-reviews .card-btn{background:var(--purple)}

.divider{left:0;width:1200px;height:1px;background:var(--line)}

/* scoring */
.panel{border:1px solid var(--line)}
.scoring{left:73px;top:1089px;width:511px;height:226px}
.panel-head{height:54px;padding:0 17px;display:flex;align-items:center;color:#fff;font-size:21px;font-weight:500}
.scoring .panel-head{background:var(--orange)}
.score-row{display:grid;grid-template-columns:55px 146px 120px 190px;align-items:center;height:57px;padding-left:18px;font-size:13px;color:#444;border-bottom:1px solid var(--line)}
.score-row:last-child{border-bottom:none}
.score-row .stars{font-size:16px}
.feedback{background:var(--red);color:#fff;height:32px;width:142px;border-radius:3px;font-size:13px;display:flex;align-items:center;justify-content:center;gap:6px}
.profile-facts{left:614px;top:1089px;width:513px;height:226px}
.profile-facts .panel-head{background:var(--grey-head);font-size:13px;font-weight:500}
.fact-row,.profile-facts .panel-head{display:grid;grid-template-columns:182px 173px 140px;padding-left:18px}
.fact-row{align-items:center;height:57px;font-size:13px;color:#444;border-bottom:1px solid var(--line)}
.fact-row:last-child{border-bottom:none}
.profile-facts .panel-head span{align-self:center}

/* subjects */
.subjects{left:73px;top:1425px;width:1054px;height:338px}
.subjects .panel-head{background:var(--orange)}
.subj-row{display:grid;grid-template-columns:227px 126px 142px 110px 119px 142px 1fr;align-items:center;height:56px;padding-left:18px;font-size:13px;color:#444;border-bottom:1px solid var(--line);margin:0 18px 0 0}
.subj-head{background:var(--grey-row);height:54px;margin:0;padding-right:18px;border-bottom:none}
.subj-row:last-child{border-bottom:none}

/* availability */
.availability{left:73px;top:1874px;width:1054px;height:328px}
.availability .panel-head{background:var(--orange);justify-content:space-between}
.month{display:flex;align-items:center;gap:14px;font-size:16px;font-weight:500}
.cal{display:grid;grid-template-columns:132px repeat(7,131px);margin-top:2px}
.cal div{height:52px;display:flex;align-items:center;justify-content:center;font-size:13px;color:#444;border-right:1px solid #fff;border-bottom:1px solid #fff}
.cal .day,.cal .corner{background:var(--grey-row)}
.cal .time{background:#fff;border-right:1px solid var(--line);border-bottom:none}
.cal .a{background:var(--avail)}
.cal .t{background:var(--taken)}
.cal .r{background:var(--reserved)}
.cal .n{background:var(--no)}
.legend{display:flex;justify-content:center;gap:36px;margin-top:18px;font-size:12px;color:#444}
.legend span{display:flex;align-items:center;gap:9px}
.legend i{width:15px;height:15px;display:block}

/* reviews */
.reviews-band{left:0;top:2258px;width:1200px;height:501px;background:linear-gradient(180deg,#5a3a22 0%,#6f4a2a 45%,#4b3120 100%)}
.reviews-title{left:0;top:2306px;width:1200px;text-align:center;color:#fff;font-size:22px;font-weight:500}
.reviews-title::after{content:"";display:block;width:34px;height:3px;background:var(--orange);margin:14px auto 0}
.review{top:2446px;width:334px;height:257px;background:#fff;text-align:center;padding-top:60px}
.avatar{position:absolute;left:127px;top:-36px;width:80px;height:80px;border:4px solid #fff;background:linear-gradient(180deg,#c9b6a4,#8f7a6a)}
.review h3{font-size:18px;font-weight:500;color:#222}
.review .stars{font-size:15px;margin-top:6px}
.review small{display:block;font-size:12px;color:#555;margin-top:2px}
.review p{font-size:13px;line-height:20px;color:#333;padding:0 30px;margin-top:16px}

/* footer */
.site-footer{left:0;top:2759px;width:1200px;height:371px;background:var(--footer)}
.foot-col{top:2814px}
.foot-col h4{color:var(--orange);font-size:16px;font-weight:500;margin-bottom:18px}
.foot-col p,.foot-col li{font-size:13px;color:#444;line-height:26px;list-style:none}
.news-label{font-size:13px;color:#444;margin-top:10px;padding-bottom:4px;border-bottom:1px solid #ccc;width:243px}
.subscribe{width:243px;height:47px;background:var(--orange);margin-top:22px}
.socials{display:flex;gap:8px;margin-top:18px}
.socials i{width:35px;height:35px;border-radius:50%;display:block}
.copyright{left:0;top:3070px;width:1200px;text-align:center;font-size:13px;color:#555;border-top:1px solid #e2e2e2;padding-top:0}
</style>
</head>
<body>

<header class="site-header abs">
  <div class="brand abs"><span class="brand-mark"></span>LendYourLessons</div>
  <nav class="main-nav abs">
    <a class="active" style="left:0">Home</a>
    <a style="left:69px">Search</a>
    <a style="left:152px">Student</a>
    <a style="left:251px">Tutor</a>
    <a style="left:326px">About</a>
    <a style="left:403px">Contact</a>
  </nav>
  <div class="login abs">
    <svg width="14" height="14" viewBox="0 0 14 14"><circle cx="7" cy="4" r="3.4" fill="#f07a0a"/><path d="M0.5 14c0-4 3-6 6.5-6s6.5 2 6.5 6z" fill="#f07a0a"/></svg>
    Login or Register
  </div>
</header>

<section class="hero abs">
  <div class="hero-frame abs"></div>
  <svg class="hero-stripes abs" width="110" height="140" viewBox="0 0 110 140">
    <polygon points="40,0 62,0 22,140 0,140" fill="#f07a0a"/>
    <polygon points="76,0 98,0 58,140 36,140" fill="#2e9e7a"/>
  </svg>
  <div class="hero-photo abs" role="img" aria-label="Portrait photo of the tutor, arms crossed, wearing a blue denim shirt"></div>
  <div class="hi-bubble abs">Hi.</div>
  <div class="hero-name abs">My name is Elena</div>
  <div class="hero-role abs">I am....</div>
  <p class="hero-text abs">Passionate about teaching. I Find it easy to inspire children to want learn, a gift not many people have. I am excellent English Teachear and Understand the letest teaching practices.</p>
  <a class="btn hero-btn btn-register abs">
    <svg width="14" height="14" viewBox="0 0 14 14"><path d="M1 13l1-4 8-8 3 3-8 8z" fill="#fff"/></svg>Register Today</a>
  <a class="btn hero-btn btn-video abs">
    <svg width="16" height="12" viewBox="0 0 16 12"><rect x="0" y="1" width="11" height="10" rx="1" fill="#fff"/><polygon points="11,6 16,2 16,10" fill="#fff"/></svg>Watch Our Video</a>
</section>

<section class="card card-contact abs">
  <div class="card-head">Contact Us</div>
  <div class="card-body">
    <div class="field field-subject">Subject</div>
    <div class="field field-message">Messages</div>
    <a class="btn card-btn">
      <svg width="22" height="14" viewBox="0 0 22 14"><rect x="6" y="1" width="16" height="12" fill="#fff"/><path d="M6 1l8 7 8-7" stroke="#f0b400" stroke-width="1.5" fill="none"/><rect x="0" y="4" width="4" height="1.5" fill="#fff"/><rect x="1" y="8" width="3" height="1.5" fill="#fff"/></svg>Send Message</a>
  </div>
</section>

<section class="card card-favour abs">
  <div class="card-head">Contact Favour</div>
  <div class="card-body">
    <p class="favour-lead">She Would like to know your schedule.</p>
    <ul class="ticks">
      <li><svg width="14" height="14" viewBox="0 0 14 14"><circle cx="7" cy="7" r="7" fill="#2e9e7a"/><path d="M3.5 7l2.5 2.5 4.5-5" stroke="#fff" stroke-width="1.8" fill="none"/></svg>Offline Lessons</li>
      <li><svg width="14" height="14" viewBox="0 0 14 14"><circle cx="7" cy="7" r="7" fill="#2e9e7a"/><path d="M3.5 7l2.5 2.5 4.5-5" stroke="#fff" stroke-width="1.8" fill="none"/></svg>Affordable Rates</li>
      <li><svg width="14" height="14" viewBox="0 0 14 14"><circle cx="7" cy="7" r="7" fill="#2e9e7a"/><path d="M3.5 7l2.5 2.5 4.5-5" stroke="#fff" stroke-width="1.8" fill="none"/></svg>1-on-1 Tutoring</li>
      <li><svg width="14" height="14" viewBox="0 0 14 14"><circle cx="7" cy="7" r="7" fill="#2e9e7a"/><path d="M3.5 7l2.5 2.5 4.5-5" stroke="#fff" stroke-width="1.8" fill="none"/></svg>Refund Policy</li>
    </ul>
    <a class="btn card-btn">
      <svg width="14" height="14" viewBox="0 0 14 14"><polygon points="0,6 14,0 9,14 7,8" fill="#fff"/></svg>Contact Favour</a>
  </div>
</section>

<section class="card card-reviews abs">
  <div class="card-head">Customer Reviews</div>
  <div class="card-body">
    <div class="rating-line"><span class="stars">★★★★★</span>15 (5.0 out of 5 stars)</div>
    <div class="bars">
      <div class="bar-row"><span>5 Star</span><div class="bar"><i style="width:100%"></i></div><span>100%</span></div>
      <div class="bar-row"><span>4 Star</span><div class="bar"><i style="width:0"></i></div><span>0%</span></div>
      <div class="bar-row"><span>3 Star</span><div class="bar"><i style="width:0"></i></div><span>0%</span></div>
      <div class="bar-row"><span>2 Star</span><div class="bar"><i style="width:0"></i></div><span>0%</span></div>
      <div class="bar-row"><span>1 Star</span><div class="bar"><i style="width:0"></i></div><span>0%</span></div>
    </div>
    <p class="share-note">Share your thoughts with other customers</p>
    <a class="btn card-btn">
      <svg width="14" height="14" viewBox="0 0 14 14"><path d="M1 13l1-4 8-8 3 3-8 8z" fill="#fff"/></svg>Write a Review</a>
  </div>
</section>

<div class="divider abs" style="top:1033px"></div>

<section class="scoring panel abs">
  <div class="panel-head">Scoring</div>
  <div class="score-row"><span>Review Score</span><span class="stars">★★★★★</span><span>4.5/5</span><span>Member Since</span></div>
  <div class="score-row"><span>Reliability</span><span class="stars">★★★★<span class="off">★</span></span><span>4.0/5</span><span>Last Logged In</span></div>
  <div class="score-row"><span>Punctuality</span><span class="stars">★★★★★</span><span>4.6/5</span><span class="feedback"><svg width="12" height="12" viewBox="0 0 14 14"><polygon points="0,6 14,0 9,14 7,8" fill="#fff"/></svg>Leave Feedback</span></div>
</section>

<section class="profile-facts panel abs">
  <div class="panel-head"><span>Tutoring Type</span><span>In Personal Only</span><span>Teacher</span></div>
  <div class="fact-row"><span>Willing To Travel</span><span>Home Only</span><span>Full Time Tutor</span></div>
  <div class="fact-row"><span>Age</span><span>20</span><span>Full Time Student</span></div>
  <div class="fact-row"><span>DBS (CRB)</span><span></span><span></span></div>
</section>

<div class="divider abs" style="top:1367px"></div>

<section class="subjects panel abs">
  <div class="panel-head">Subject Taught</div>
  <div class="subj-row subj-head"><span></span><span>Primary</span><span>Secondary</span><span>GCSE</span><span>A-level</span><span>University</span><span>Adult Learner</span></div>
  <div class="subj-row"><span>Biology</span><span>£20</span><span>£20</span><span>£50</span><span></span><span>£20</span><span>£20</span></div>
  <div class="subj-row"><span>Chemistry</span><span>£20</span><span>£30</span><span>£20</span><span></span><span>£20</span><span>£20</span></div>
  <div class="subj-row"><span>Chemistry</span><span>£20</span><span>£30</span><span>£20</span><span></span><span>£20</span><span>£20</span></div>
  <div class="subj-row"><span>Chemistry</span><span>£20</span><span>£30</span><span>£20</span><span></span><span>£20</span><span>£20</span></div>
</section>

<div class="divider abs" style="top:1815px"></div>

<section class="availability panel abs">
  <div class="panel-head">Availability
    <span class="month">December 2016
      <svg width="40" height="14" viewBox="0 0 40 14"><path d="M6 2l-5 5 5 5" stroke="#fff" stroke-width="1.6" fill="none"/><rect x="14" y="2" width="11" height="11" fill="#fff"/><rect x="16" y="6" width="7" height="5" fill="#f07a0a"/><path d="M34 2l5 5-5 5" stroke="#fff" stroke-width="1.6" fill="none"/></svg>
    </span>
  </div>
  <div class="cal">
    <div class="corner"></div><div class="day">Mon (7th)</div><div class="day">Tue (8th)</div><div class="day">Wed (9th)</div><div class="day">Thu (10th)</div><div class="day">Fri (11th)</div><div class="day">Sat (12th)</div><div class="day">Sun (13th)</div>
    <div class="time">7-8PM</div><div class="a"></div><div class="a"></div><div class="t"></div><div class="a"></div><div class="a"></div><div class="a"></div><div class="a"></div>
    <div class="time">8-9PM</div><div class="a"></div><div class="a"></div><div class="r"></div><div class="a"></div><div class="a"></div><div class="a"></div><div class="n"></div>
    <div class="time">4-5PM</div><div class="a"></div><div class="a"></div><div class="n"></div><div class="a"></div><div class="r"></div><div class="a"></div><div class="a"></div>
  </div>
  <div class="legend">
    <span><i style="background:var(--avail)"></i>Available</span>
    <span><i style="background:var(--taken)"></i>Taken</span>
    <span><i style="background:var(--reserved)"></i>Reserved</span>
    <span><i style="background:var(--no)"></i>No</span>
  </div>
</section>

<section class="reviews-band abs" role="img" aria-label="Warm sepia-toned photo of a group of smiling students"></section>
<h2 class="reviews-title abs">Tutors Reviews</h2>

<article class="review abs" style="left:73px">
  <div class="avatar" role="img" aria-label="Photo of reviewer Maren"></div>
  <h3>Maren</h3>
  <div class="stars">★★★<span class="off">★★</span></div>
  <small>(Star Rateing 3)</small>
  <p>" Reference site about Lorem Ipsum, giving information on its origins, as well as a random Lipsum generator."</p>
</article>
<article class="review abs" style="left:434px">
  <div class="avatar" role="img" aria-label="Photo of reviewer Tom Archer"></div>
  <h3>Tom Archer</h3>
  <div class="stars">★★★<span class="off">★★</span></div>
  <small>(Star Rateing 3)</small>
  <p>" Reference site about Lorem Ipsum, giving information on its origins, as well as a random Lipsum generator."</p>
</article>
<article class="review abs" style="left:793px">
  <div class="avatar" role="img" aria-label="Photo of reviewer Priya"></div>
  <h3>Priya</h3>
  <div class="stars">★★★<span class="off">★★</span></div>
  <small>(Star Rateing 3)</small>
  <p>" Reference site about Lorem Ipsum, giving information on its origins, as well as a random Lipsum generator."</p>
</article>

<footer class="site-footer abs"></footer>
<div class="foot-col abs" style="left:73px">
  <h4>Get Our Newsletter</h4>
  <p style="line-height:20px">To receive updates about my tutor,<br>Join our newsletter.</p>
  <div class="news-label">Name</div>
  <div class="news-label">Email</div>
  <a class="btn subscribe">Subscribe</a>
</div>
<div class="foot-col abs" style="left:434px">
  <h4>Contact Us</h4>
  <p style="line-height:20px">228 Lorem Ipsum dolor,<br>Dosis amet, -85485</p>
  <p style="line-height:20px;margin-top:16px">T: 1800 555 01<br>E: info@lendyourlessons.com</p>
  <div class="socials"><i style="background:#3b5998"></i><i style="background:#2aa3ef"></i><i style="background:#dd4b39"></i></div>
</div>
<div class="foot-col abs" style="left:705px">
  <h4>Quick Links</h4>
  <ul><li>Home</li><li>Search</li><li>Student</li><li>Tutor</li><li>About</li><li>Contact</li></ul>
</div>
<div class="foot-col abs" style="left:885px">
  <h4>Info Links</h4>
  <ul><li>Register as a Student</li><li>Register as a Paretnt</li><li>Register as a Tutor</li></ul>
</div>
<p class="copyright abs"><span style="display:block;padding-top:12px">Copyright 2016 Lend Your Lessons. All Rights Reserved.</span></p>

</body>
</html>
```